Institute for Hollow Relief at Annapolis
business card and stationary
Institute for Hollow Relief at Annapolis -
Creative Brief
Professional
Dominic T. Halloway, MD
472 Fenwick Court, Suite 208 Annapolis, MD 21409
dthalloway82@mailbright.example
www.wombrelief.example
Use new logo Comprehensive Gynecologic Care with Specialization in Chronic Pain Disorders and Minimally Invasive Surgery
Appointment Date and Time: Mon. _______ Tue _____ Wed ______ Thurs_______ Fri_______ _______ AM _______ PM

```html
<!DOCTYPE html>
<html lang="en">
<head>
<meta charset="utf-8">
<title>Institute for Hollow Relief at Annapolis — Stationery</title>
<link href="https://fonts.googleapis.com/css2?family=Lato:wght@400;700&display=swap" rel="stylesheet">
<style>
  :root {
    --board: #2e2e2f;
    --paper: #ffffff;
    --plum: #a3679d;
    --plum-light: #c99bc4;
    --plum-faint: #f1e6ef;
    --slate: #5b5b5e;
    --ink: #6a6a6a;
    --caption: #9a9a9a;
  }
  * { box-sizing: border-box; margin: 0; padding: 0; }
  html, body { width: 1200px; height: 338px; overflow: hidden; background: var(--board); }
  body { position: relative; font-family: "Lato", Arial, sans-serif; color: var(--ink); }

  .piece { position: absolute; background: var(--paper); overflow: hidden; box-shadow: 0 1px 3px rgba(0,0,0,.5); }
  .piece svg.swoosh { position: absolute; inset: 0; width: 100%; height: 100%; }
  .caption { position: absolute; font-size: 4px; color: var(--caption); letter-spacing: .2px; white-space: nowrap; }

  .brand { position: absolute; display: flex; align-items: center; gap: 3px; }
  .brand .dot { width: 9px; height: 9px; border-radius: 50%; background: var(--plum); flex: none; }
  .brand .name { font-size: 4px; line-height: 1.15; color: var(--plum); font-weight: 700; max-width: 46px; }

  .tiny { position: absolute; font-size: 3.4px; line-height: 1.35; color: var(--ink); }
  .faint-mark { position: absolute; border-radius: 50%; background: var(--plum-faint); }

  /* business cards */
  .card-front { left: 14px; top: 186px; width: 52px; height: 38px; }
  .card-back  { left: 14px; top: 244px; width: 52px; height: 38px; }
  .card-back .line { position: absolute; left: 5px; right: 5px; height: .5px; background: #ccc; }

  /* letterheads */
  .letterhead-one { left: 92px; top: 14px; width: 266px; height: 302px; }
  .letterhead-two { left: 382px; top: 14px; width: 222px; height: 302px; }

  /* envelopes */
  .envelope-one { left: 630px; top: 42px; width: 262px; height: 108px; }
  .envelope-two { left: 630px; top: 172px; width: 262px; height: 110px; }

  .envelope-back { position: absolute; left: 913px; width: 276px; overflow: hidden; }
  .back-plum  { top: 14px; height: 58px; background: var(--plum); }
  .back-slate { top: 74px; height: 50px; background: var(--slate); }
  .back-white { top: 126px; height: 190px; background: var(--paper); }
  .envelope-back .seal { position: absolute; left: 50%; top: 50%; width: 12px; height: 12px; margin: -6px 0 0 -6px; border-radius: 50%; background: var(--paper); }
  .back-white .seal { background: var(--plum); top: 14px; margin-top: 0; }
</style>
</head>
<body>

  <!-- Business card front -->
  <section class="piece card-front">
    <svg class="swoosh" viewBox="0 0 52 38" preserveAspectRatio="none" aria-hidden="true">
      <path d="M30 0 Q48 2 52 16 L52 0 Z" fill="var(--plum)"/>
    </svg>
    <div class="brand" style="left:4px; top:5px;"><span class="dot" style="width:6px;height:6px"></span><span class="name" style="font-size:2.6px;max-width:26px">Institute for Hollow Relief at Annapolis</span></div>
    <div class="tiny" style="left:4px; top:20px; font-size:2.4px;">Dominic T. Halloway, MD<br>472 Fenwick Court, Suite 208<br>Annapolis, MD 21409<br>www.wombrelief.example</div>
  </section>
  <div class="caption" style="left:14px; top:227px;">Business Card Front</div>

  <!-- Business card back -->
  <section class="piece card-back">
    <div class="tiny" style="left:5px; top:4px; font-size:2.4px; color:var(--plum); font-weight:700;">Appointment Date and Time:</div>
    <div class="line" style="top:12px"></div>
    <div class="line" style="top:17px"></div>
    <div class="line" style="top:22px"></div>
    <div class="line" style="top:27px"></div>
    <div class="tiny" style="left:5px; top:30px; font-size:2.2px;">___ AM ___ PM</div>
  </section>
  <div class="caption" style="left:14px; top:285px;">Business Card Back</div>

  <!-- Letterhead version one -->
  <section class="piece letterhead-one">
    <svg class="swoosh" viewBox="0 0 266 302" preserveAspectRatio="none" aria-hidden="true">
      <path d="M170 0 Q250 6 266 70 L266 0 Z" fill="var(--plum)"/>
      <path d="M0 248 Q14 292 110 302 L0 302 Z" fill="var(--plum)"/>
    </svg>
    <div class="brand" style="left:14px; top:12px;"><span class="dot"></span><span class="name">Institute for Hollow Relief at Annapolis</span></div>
    <div class="tiny" style="left:130px; top:13px;">Dominic T. Halloway, MD<br>472 Fenwick Court, Suite 208<br>Annapolis, MD 21409<br>dthalloway82@mailbright.example</div>
    <div class="faint-mark" style="left:93px; top:100px; width:80px; height:80px;"></div>
  </section>
  <div class="caption" style="left:92px; top:319px;">Letterhead Version 1</div>

  <!-- Letterhead version two -->
  <section class="piece letterhead-two">
    <svg class="swoosh" viewBox="0 0 222 302" preserveAspectRatio="none" aria-hidden="true">
      <path d="M120 0 Q214 10 222 120 L222 0 Z" fill="var(--plum)"/>
      <path d="M110 0 Q212 16 218 150" fill="none" stroke="var(--plum-light)" stroke-width="1.2"/>
      <path d="M0 230 Q20 292 130 302 L0 302 Z" fill="var(--plum)"/>
      <path d="M0 222 Q26 288 140 300" fill="none" stroke="var(--plum-light)" stroke-width="1.2"/>
    </svg>
    <div class="brand" style="left:12px; top:12px;"><span class="dot"></span><span class="name">Institute for Hollow Relief at Annapolis</span></div>
    <div class="faint-mark" style="left:71px; top:100px; width:80px; height:80px;"></div>
    <div class="tiny" style="left:0; right:0; bottom:5px; text-align:center; font-size:3px;">472 Fenwick Court, Suite 208 Annapolis, MD 21409 · www.wombrelief.example</div>
  </section>
  <div class="caption" style="left:382px; top:319px;">Letterhead Version 2</div>

  <!-- Envelope version one -->
  <section class="piece envelope-one">
    <svg class="swoosh" viewBox="0 0 262 108" preserveAspectRatio="none" aria-hidden="true">
      <path d="M262 20 Q250 96 140 108 L262 108 Z" fill="var(--plum)"/>
    </svg>
    <div class="brand" style="left:10px; top:9px;"><span class="dot"></span><span class="name">Institute for Hollow Relief at Annapolis</span></div>
    <div class="tiny" style="left:10px; top:24px;">472 Fenwick Court, Suite 208<br>Annapolis, MD 21409</div>
  </section>
  <div class="caption" style="left:630px; top:153px;">Envelope Version 1</div>

  <!-- Envelope version two -->
  <section class="piece envelope-two">
    <svg class="swoosh" viewBox="0 0 262 110" preserveAspectRatio="none" aria-hidden="true">
      <path d="M262 30 Q254 100 170 110 L262 110 Z" fill="var(--plum)"/>
      <path d="M258 20 Q256 98 150 108" fill="none" stroke="var(--plum-light)" stroke-width="1"/>
    </svg>
    <div class="brand" style="left:10px; top:9px;"><span class="dot"></span><span class="name">Institute for Hollow Relief at Annapolis</span></div>
    <div class="tiny" style="left:10px; top:24px;">472 Fenwick Court, Suite 208<br>Annapolis, MD 21409</div>
  </section>
  <div class="caption" style="left:630px; top:285px;">Envelope Version 2</div>

  <!-- Envelope backs -->
  <section class="envelope-back back-plum"><span class="seal"></span></section>
  <section class="envelope-back back-slate"><span class="seal"></span></section>
  <section class="envelope-back back-white">
    <svg class="swoosh" viewBox="0 0 276 190" preserveAspectRatio="none" aria-hidden="true" style="position:absolute;inset:0;width:100%;height:100%">
      <path d="M0 0 L138 70 L276 0" fill="none" stroke="#dcdcdc" stroke-width="1"/>
      <path d="M0 190 L120 110 M276 190 L156 110" fill="none" stroke="#e4e4e4" stroke-width="1"/>
    </svg>
    <span class="seal"></span>
  </section>
  <div class="caption" style="left:913px; top:319px;">Envelope Back Versions</div>

</body>
</html>
```